Brand New Upscale OOBGYN Office

Im in Need of an advertising one sided postcard as soon as possible. It's for a brand new OBGYN office in the Northern Virginia area. We are trying to create a new patient customer base. I have attached photos of the inside of the office and logos. The office contact information needs to be on the postcard. You can find that on the attached pdf file named business card. That same file is the font that needs to be used. The font is called TT Drugs. Please contact me with any questions. I would appreciated it so much if you could send me these proofs as soon as possible. Thank you!!!
Women
Advertising
- TT Drugs

```html
<!DOCTYPE html>
<html lang="en">
<head>
<meta charset="utf-8">
<title>Harborview OBGYN Postcard</title>
<link rel="stylesheet" href="https://fonts.googleapis.com/css2?family=Roboto+Condensed:wght@300;400&family=Arimo:wght@400&display=swap">
<style>
  :root {
    --backdrop: #e9e6e2;
    --brand-blue: #1f4fb4;
    --ink: #1c1c1c;
    --grey: #8a8a8a;
    --light-grey: #d4d4d4;
    --white: #ffffff;
    --photo-warm: #e7d2c4;
    --photo-cool: #cfdbe6;
  }
  html, body { margin: 0; padding: 0; overflow: hidden; }
  body {
    width: 900px; height: 1200px;
    background: var(--backdrop);
    position: relative;
    font-family: "Roboto Condensed", sans-serif;
  }
  .postcard {
    position: absolute;
    background: var(--white);
    overflow: hidden;
    box-shadow: 0 6px 18px rgba(0,0,0,.25);
  }
  .postcard--front { left: 167px; top: 90px; width: 566px; height: 437px; }
  .postcard--back  { left: 170px; top: 665px; width: 560px; height: 432px; }
  .postcard__art { position: absolute; inset: 0; }
  .brand-name {
    position: absolute; margin: 0;
    font-family: "Roboto Condensed", sans-serif; font-weight: 400;
    color: var(--grey); font-size: 17px; letter-spacing: .6px; line-height: 20px;
    text-transform: uppercase;
  }
  .headline {
    position: absolute; left: 210px; top: 84px; margin: 0;
    font-weight: 400; font-size: 15.5px; line-height: 18px; text-transform: uppercase;
  }
  .headline__lead { color: var(--brand-blue); display: block; }
  .headline__sub { color: var(--grey); display: block; }
  .intro {
    position: absolute; left: 28px; top: 198px; width: 214px;
    font-family: "Arimo", sans-serif; font-size: 10.6px; line-height: 12.5px;
    color: var(--white); text-align: justify;
  }
  .intro p { margin: 0 0 8px; }
  .contact {
    position: absolute; list-style: none; margin: 0; padding: 0;
    font-family: "Arimo", sans-serif; font-size: 10.4px; line-height: 13px; color: var(--ink);
  }
  .contact li { display: flex; align-items: flex-start; gap: 6px; margin-bottom: 3px; }
  .contact svg { flex: none; width: 13px; height: 13px; fill: var(--brand-blue); }
  .postcard--front .contact { left: 22px; top: 345px; }
  .postcard--back .contact { left: 30px; top: 350px; }
  .services { position: absolute; left: 53px; top: 198px; color: var(--white); }
  .services__title { margin: 0 0 10px; font-weight: 400; font-size: 21px; letter-spacing: .3px; }
  .services__list { list-style: none; margin: 0; padding: 0; font-weight: 300; font-size: 16.5px; line-height: 20px; color: var(--white); }
  .services__list li::before {
    content: ""; display: inline-block; width: 7px; height: 7px; border-radius: 50%;
    background: var(--white); margin: 0 9px 2px 2px; vertical-align: middle;
  }
  .stamp-box { position: absolute; left: 452px; top: 26px; width: 73px; height: 73px; border: 1.5px solid var(--ink); }
  .address-line { position: absolute; left: 326px; width: 190px; height: 1px; background: #9aa7c4; }
</style>
</head>
<body>

<!-- Front of postcard -->
<section class="postcard postcard--front">
  <svg class="postcard__art" viewBox="0 0 566 437" width="566" height="437">
    <defs>
      <linearGradient id="front-sky" x1="0" y1="0" x2="1" y2="1">
        <stop offset="0" stop-color="#ffffff"/><stop offset="1" stop-color="#ececec"/>
      </linearGradient>
      <linearGradient id="front-blue" x1="0" y1="0" x2="0" y2="1">
        <stop offset="0" stop-color="#2a5cc4"/><stop offset="1" stop-color="#173f9e"/>
      </linearGradient>
      <linearGradient id="front-photo" x1="0" y1="0" x2="1" y2="1">
        <stop offset="0" stop-color="#f2f3f5"/><stop offset=".6" stop-color="#e7d2c4"/><stop offset="1" stop-color="#cfdbe6"/>
      </linearGradient>
      <radialGradient id="front-baby" cx=".5" cy=".5" r=".6">
        <stop offset="0" stop-color="#efd9cc"/><stop offset="1" stop-color="#b59788"/>
      </radialGradient>
    </defs>
    <rect width="566" height="437" fill="url(#front-sky)"/>
    <path d="M0,84 Q300,300 566,88 L566,332 L0,332 Z" fill="url(#front-blue)"/>
    <path d="M0,72 Q300,288 566,74 L566,84 Q300,298 0,80 Z" fill="var(--white)"/>
    <path d="M0,50 Q300,262 566,52 L566,64 Q300,276 0,62 Z" fill="var(--light-grey)"/>
    <path d="M0,64 Q300,278 566,66" fill="none" stroke="var(--ink)" stroke-width="4"/>
    <rect y="332" width="566" height="85" fill="#f6f6f6"/>
    <rect y="417" width="566" height="20" fill="var(--brand-blue)"/>
    <path d="M232,437 C248,300 330,185 566,150 L566,437 Z" fill="var(--white)"/>
    <path d="M244,437 C260,306 338,196 566,162 L566,437 Z" fill="var(--ink)"/>
    <g role="img" aria-label="Photo of a doctor with a clipboard beside a smiling pregnant patient">
      <path d="M252,437 C268,312 344,204 566,170 L566,437 Z" fill="url(#front-photo)"/>
    </g>
    <circle cx="98" cy="90" r="71" fill="var(--white)"/>
    <circle cx="98" cy="90" r="66" fill="var(--ink)"/>
    <g role="img" aria-label="Photo of a sleeping newborn resting beside its mother">
      <circle cx="98" cy="90" r="61" fill="url(#front-baby)"/>
    </g>
  </svg>

  <p class="brand-name" style="left:232px; top:36px;">Harborview OBGYN</p>

  <h1 class="headline">
    <span class="headline__lead">Harborview OBGYN is Northern Virginia's</span>
    <span class="headline__sub">Premiere Womens Health Center</span>
  </h1>

  <div class="intro">
    <p>Harborview OBGYN, we are dedicated to provide comprehensive, excellent women's health services in a compassionate profes-</p>
    <p>We have an extensive range and depth of expertise in general obstetrics and gynecol­ogy. We are committed to staying abreast of the newest technology and guidelines for essential preventive health care.</p>
  </div>

  <ul class="contact">
    <li><svg viewBox="0 0 16 16"><path d="M8 1 0 8h2v7h4v-5h4v5h4V8h2z"/></svg><span>4512 Meadow Lane, Suite 105<br>Fairbrook, VA 20999</span></li>
    <li><svg viewBox="0 0 16 16"><path d="M1 1h14v14H1z M5 4c-1 1 0 4 3 7s5 3 6 2l-2-2-1.5 1C9 11 6.5 8 6 7l1-1.5z" fill-rule="evenodd"/></svg><span>703-555-0142</span></li>
    <li><svg viewBox="0 0 16 16"><circle cx="8" cy="8" r="7" fill="none" stroke="#1f4fb4" stroke-width="1.4"/><path d="M1 8h14M8 1c-3 3-3 11 0 14M8 1c3 3 3 11 0 14" fill="none" stroke="#1f4fb4" stroke-width="1.2"/></svg><span>HarborviewOBGYN.com</span></li>
  </ul>
</section>

<!-- Back of postcard -->
<section class="postcard postcard--back">
  <svg class="postcard__art" viewBox="0 0 560 432" width="560" height="432">
    <defs>
      <linearGradient id="back-band" x1="0" y1="1" x2="1" y2="0">
        <stop offset="0" stop-color="#e2e2e2"/><stop offset="1" stop-color="#f7f7f7"/>
      </linearGradient>
      <linearGradient id="back-blue" x1="0" y1="0" x2="0" y2="1">
        <stop offset="0" stop-color="#2a5cc4"/><stop offset="1" stop-color="#173f9e"/>
      </linearGradient>
      <linearGradient id="back-photo" x1="0" y1="0" x2="0" y2="1">
        <stop offset="0" stop-color="#6b3a2a"/><stop offset=".55" stop-color="#2a1a16"/><stop offset="1" stop-color="#0d0d10"/>
      </linearGradient>
    </defs>
    <rect width="560" height="432" fill="var(--white)"/>
    <path d="M0,118 Q210,95 300,0 L322,0 Q235,140 0,168 Z" fill="url(#back-band)"/>
    <path d="M0,172 Q240,140 322,0 L336,0 Q330,215 282,340 L0,340 Z" fill="url(#back-blue)"/>
    <path d="M344,0 L356,0 Q348,225 292,340 L284,340 Q336,220 344,0 Z" fill="var(--brand-blue)"/>
    <rect y="340" width="300" height="78" fill="#f4f4f4"/>
    <path d="M0,418 L300,418 L296,432 L0,432 Z" fill="var(--brand-blue)"/>
    <circle cx="227" cy="130" r="76" fill="var(--white)"/>
    <circle cx="227" cy="130" r="71" fill="var(--brand-blue)"/>
    <g role="img" aria-label="Photo of the office reception desk in front of a lit wood wall">
      <circle cx="227" cy="130" r="66" fill="url(#back-photo)"/>
    </g>
  </svg>

  <p class="brand-name" style="left:24px; top:24px;">Harborview OBGYN</p>

  <div class="services">
    <h2 class="services__title">SERVICES</h2>
    <ul class="services__list">
      <li>Obstetric and Prenatal Services</li>
      <li>Gynecologic Services</li>
      <li>Infertility Services</li>
      <li>Surgical Services</li>
    </ul>
  </div>

  <ul class="contact">
    <li><svg viewBox="0 0 16 16"><path d="M8 1 0 8h2v7h4v-5h4v5h4V8h2z"/></svg><span>4512 Meadow Lane, Suite 105<br>Fairbrook, VA 20999</span></li>
    <li><svg viewBox="0 0 16 16"><path d="M1 1h14v14H1z M5 4c-1 1 0 4 3 7s5 3 6 2l-2-2-1.5 1C9 11 6.5 8 6 7l1-1.5z" fill-rule="evenodd"/></svg><span>703-555-0142</span></li>
    <li><svg viewBox="0 0 16 16"><circle cx="8" cy="8" r="7" fill="none" stroke="#1f4fb4" stroke-width="1.4"/><path d="M1 8h14M8 1c-3 3-3 11 0 14M8 1c3 3 3 11 0 14" fill="none" stroke="#1f4fb4" stroke-width="1.2"/></svg><span>HarborviewOBGYN.com</span></li>
  </ul>

  <div class="stamp-box"></div>
  <div class="address-line" style="top:223px;"></div>
  <div class="address-line" style="top:258px;"></div>
  <div class="address-line" style="top:297px;"></div>
</section>

</body>
</html>
```